PELDRAX Business Cards

We require a business card for our company that provides IT consulting services. We already have a logo that needs to be used on the card. We want a clean professional looking design that incorporates our colours. Our main focus is providing managed services to business, which involves us looking after all of their IT requirements including managing servers/networks, projects, and procurement.

Industry/Entity Type

Information Technology

Requirements
Must have
• our logo, contact information, name, title, phone numbers

```html
<!DOCTYPE html>
<html lang="en">
<head>
<meta charset="utf-8">
<title>PELDRAX Business Card</title>
<link rel="stylesheet" href="https://fonts.googleapis.com/css2?family=Roboto:wght@400;500;700&display=swap">
<style>
  :root {
    --page-bg: #e9e4dc;
    --card-top: #e6eef3;
    --card-top-edge: #d3dfe7;
    --brand-blue: #1d6fa3;
    --band-blue: #1f7fb0;
    --band-blue-deep: #14618f;
    --text-light: #dfe6ec;
    --text-soft: #cfdbe4;
  }
  html, body {
    margin: 0;
    padding: 0;
    width: 1200px;
    height: 970px;
    overflow: hidden;
    background: var(--page-bg);
    font-family: "Roboto", Arial, sans-serif;
  }
  .business-card {
    position: absolute;
    left: 176px;
    top: 250px;
    width: 848px;
    height: 472px;
    border-radius: 22px;
    overflow: hidden;
    background: linear-gradient(180deg, var(--card-top) 0%, var(--card-top-edge) 100%);
    box-shadow: 0 8px 30px rgba(0,0,0,0.12);
  }
  .brand-name {
    position: absolute;
    left: 68px;
    top: 80px;
    margin: 0;
    font-size: 58px;
    font-weight: 500;
    letter-spacing: 3px;
    color: var(--brand-blue);
    line-height: 1;
  }
  .contact-band {
    position: absolute;
    left: 0;
    top: 200px;
    width: 100%;
    height: 272px;
    background: linear-gradient(180deg, var(--band-blue) 0%, var(--band-blue-deep) 100%);
  }
  .person-name {
    position: absolute;
    left: 62px;
    top: 30px;
    margin: 0;
    font-size: 24px;
    font-weight: 700;
    letter-spacing: 0.5px;
    color: var(--text-light);
  }
  .person-title {
    position: absolute;
    left: 62px;
    top: 60px;
    margin: 0;
    font-size: 18px;
    color: var(--text-soft);
  }
  .postal-address {
    position: absolute;
    left: 62px;
    top: 94px;
    margin: 0;
    font-style: normal;
    font-size: 18px;
    line-height: 24px;
    color: var(--text-soft);
  }
  .contact-list {
    position: absolute;
    left: 62px;
    top: 156px;
    margin: 0;
    padding: 0;
    list-style: none;
    font-size: 18px;
    line-height: 24px;
    color: var(--text-soft);
  }
  .contact-item {
    display: flex;
    align-items: center;
    gap: 12px;
  }
  .contact-icon {
    width: 15px;
    height: 15px;
    flex: none;
  }
</style>
</head>
<body>
  <section class="business-card">
    <h1 class="brand-name">PELDRAX</h1>

    <div class="contact-band">
      <h2 class="person-name">DANIEL HARWOOD</h2>
      <p class="person-title">President</p>

      <address class="postal-address">
        48 Cedar Avenue, PO Box 702<br>
        Millbrook, AB, T0K 3B1
      </address>

      <ul class="contact-list">
        <li class="contact-item">
          <svg class="contact-icon" viewBox="0 0 16 16" aria-hidden="true">
            <path d="M3 1.5l3 0.5 1 3.2-1.7 1.3a9 9 0 0 0 4.2 4.2L10.8 9l3.2 1 0.5 3-2 1.5C7 14 2 9 1.5 3.5z" fill="none" stroke="#cfdbe4" stroke-width="1.3" stroke-linejoin="round"/>
          </svg>
          <span>403-555-0182</span>
        </li>
        <li class="contact-item">
          <svg class="contact-icon" viewBox="0 0 16 16" aria-hidden="true">
            <rect x="1.5" y="3.5" width="13" height="9" fill="none" stroke="#cfdbe4" stroke-width="1.3"/>
            <path d="M1.5 3.5L8 9l6.5-5.5" fill="none" stroke="#cfdbe4" stroke-width="1.3"/>
          </svg>
          <span>info@peldrax.com</span>
        </li>
        <li class="contact-item">
          <svg class="contact-icon" viewBox="0 0 16 16" aria-hidden="true">
            <circle cx="8" cy="8" r="6.3" fill="none" stroke="#cfdbe4" stroke-width="1.3"/>
            <ellipse cx="8" cy="8" rx="2.8" ry="6.3" fill="none" stroke="#cfdbe4" stroke-width="1.1"/>
            <path d="M1.7 8h12.6M2.6 5h10.8M2.6 11h10.8" stroke="#cfdbe4" stroke-width="1"/>
          </svg>
          <span>www.peldrax.com</span>
        </li>
      </ul>
    </div>
  </section>
</body>
</html>
```